Menu Design for Indian Restaurant

We are a new Indian restaurant, named Saffron Lantern Restaurant, looking for a sophisticated looking menu. It is a semi-formal dining restaurant with wooden tables and chairs and will have a focus on a creating a lively atmosphere. Environment-friendly products will be used, and the menu will be 100% vegetarian. There will be an emphasis on fresh, healthy and delicious food. We will be targeting vegans, vegetarians, health conscious people, people from all age groups, Indians, Australian's as well as other ethnic communities. We need a clean, simple, sophisticated design for the new restaurant menu. Attached is the restaurant logo for reference.

UPDATE:
- We have attached the menu
- We are not looking for any particular type of layout or size (open to suggests). Please suggest this after having a look at the menu contents. However, we will be having one formal menu to be used in the restaurant, and one in brochure form for distribution.
- There are no images at present. If you feel the need of images, please use sample images for now.

Thank you for the entries thus far.
Updates

Target Market(s)

All age groups from different nationalities

Industry/Entity Type

Indian Restaurant

Colors

Designer to choose colors to be used in the design.

Requirements
Nice to have
• This will be printed on environmentally friendly paper.

```html
<!DOCTYPE html>
<html lang="en">
<head>
<meta charset="utf-8">
<title>Saffron Lantern Restaurant — Menu Cover</title>
<link href="https://fonts.googleapis.com/css2?family=Lato:wght@700&family=Cinzel:wght@400&display=swap" rel="stylesheet">
<style>
  :root {
    --backdrop: #e6e6e6;
    --paper: #ffffff;
    --paper-shade: #f3f3f3;
    --leaf-band: #c3d88a;
    --ornament-tint: #e3edc9;
    --ink: #111111;
    --dish-saffron: #e8b530;
    --dish-plate: #f4f4f4;
  }
  * { box-sizing: border-box; margin: 0; padding: 0; }
  html, body {
    width: 1200px;
    height: 912px;
    overflow: hidden;
    background: var(--backdrop);
  }
  .menu-spread {
    position: absolute;
    left: 120px;
    top: 106px;
    width: 960px;
    height: 700px;
    display: flex;
    box-shadow: 0 14px 30px rgba(0,0,0,0.12);
  }
  .menu-page {
    position: relative;
    width: 480px;
    height: 700px;
    background: var(--paper);
  }
  .menu-page--back {
    background: linear-gradient(90deg, var(--paper) 0%, var(--paper) 85%, var(--paper-shade) 100%);
  }
  .menu-page--front .band {
    position: absolute;
    top: 0;
    bottom: 0;
    width: 16px;
    background: var(--leaf-band);
  }
  .band--spine { left: 0; }
  .band--edge { right: 0; }
  .brand-name {
    position: absolute;
    left: 0;
    right: 0;
    text-align: center;
    color: var(--ink);
    font-family: "Lato", sans-serif;
    font-weight: 700;
    letter-spacing: -0.5px;
    line-height: 1;
  }
  .brand-name .brand-main { display: block; font-size: 34px; }
  .brand-name .brand-sub {
    display: block;
    margin-top: 6px;
    font-size: 10px;
    letter-spacing: 4px;
  }
  .menu-page--back .brand-name { top: 318px; }
  .menu-page--front .brand-name { top: 248px; }
  .mandala-ornament {
    position: absolute;
    left: 140px;
    top: 0;
    width: 200px;
    height: 140px;
    border-radius: 0 0 100px 100px;
    background: var(--ornament-tint);
  }
  .dish-photo {
    position: absolute;
    left: 70px;
    top: 360px;
    width: 360px;
    height: 190px;
    border-radius: 50%;
    background: radial-gradient(ellipse at 50% 45%, var(--dish-saffron) 0%, var(--dish-saffron) 32%, var(--dish-plate) 48%, var(--dish-plate) 100%);
  }
</style>
</head>
<body>
  <main class="menu-spread">
    <section class="menu-page menu-page--back">
      <h2 class="brand-name">
        <span class="brand-main">Saffron Lantern</span>
        <span class="brand-sub">RESTAURANT</span>
      </h2>
    </section>
    <section class="menu-page menu-page--front">
      <div class="band band--spine"></div>
      <div class="band band--edge"></div>
      <div class="mandala-ornament" role="img" aria-label="Light green mandala line ornament"></div>
      <h1 class="brand-name">
        <span class="brand-main">Saffron Lantern</span>
        <span class="brand-sub">RESTAURANT</span>
      </h1>
      <div class="dish-photo" role="img" aria-label="Photo of saffron rice on a white plate with cucumber slices and fresh greens"></div>
    </section>
  </main>
</body>
</html>
```